Apple Cider

We currently export our wine throughout Asia and China, now our intention is to enter the younger 18+ age market with an Alcoholic Cider using our brand name THE LARK HOLLOW.
The Cider is in a 330 ml bottle in a Green colour and packed in clusters of 6 into a carton of 24.
The closure will be a crown twist top or Stelvin cap. Probably Red in colour
The younger market consumer has a high female content and students who need a fun and interesting label, maybe even a little risque. this market uses the product a lot as a takeaway in satchels and handbags
All wording to be in English
This is only for a bottle label
The younger market is volume orientated should the label be appealing.
Updates

You can see by our website that we have wine which is distributed throughout Asia and China. The wine market seems to be made up of the 30 plus age, probably used more at on license premises. Therefore we are not catering for the younger market which would be 18 - 30 year od group. Interstingly this group are predominantly female then there are a mix of male and female students. They want a low acholic drink with a slight carbonated ( Fizzy ) finish. The bottle size of 330 ml with an easy open twist crown cap is important, they purchase as a drink within bars etc but a lot is consumed off premise, the small bottle allows to be put into handbags and satchels. Our selection of the name THE LARK HOLLOW we hope will appeal to this group so we are looking at fun type of label, please NO NUNS MASKS! We think the label will be in the 9 cm long - 3cm wide area, as we offer both loosepacking in cartons of 24 the bottle can esily be viewed but within a 6 pack carry pack we need to overcome the indentification probably on the top of the labelor possibly a small neck band as well. We did consider using the Nun photo of holding her finger to her lips to indicat a secret or silence

Target Market(s)

18 to 35 Asian

Font styles to use
Decorative
Script

Colors

Designer to choose colors to be used in the design.

Requirements
Must have
• We are looking for a young modern and fresh label. for the younger market, we have not settled on any colour theme so its wide open to you.
Nice to have
• While we have posted an image as a guide we would want other alternatives so as to portray a secret
Should not have
• No face masks please

```html
<!DOCTYPE html>
<html lang="en">
<head>
<meta charset="utf-8">
<title>The Lark Hollow – Apple Cider Label</title>
<link rel="stylesheet" href="https://fonts.googleapis.com/css2?family=Rye&family=Roboto+Condensed:wght@700&display=swap">
<style>
  :root {
    --bg: #e6ebec;
    --label-green: #a9cf4e;
    --label-green-line: #93bb3a;
    --oval-orange: #ef7a2a;
    --oval-orange-deep: #e0601c;
    --frame-white: #ffffff;
    --title-red: #a3202c;
    --pill-red: #a8262e;
    --lock-gold: #c9a83a;
    --lock-olive: #4f4a1e;
    --apple-red: #c8302c;
    --ink: #1f1a12;
  }
  * { box-sizing: border-box; margin: 0; padding: 0; }
  html, body { width: 1200px; height: 901px; overflow: hidden; }
  body {
    background: var(--bg);
    position: relative;
    font-family: "Roboto Condensed", Arial, sans-serif;
  }
  .striped {
    background: repeating-linear-gradient(
      to bottom,
      var(--label-green) 0 5px,
      var(--label-green-line) 5px 7px
    );
  }

  /* Neck band */
  .neck-band {
    position: absolute;
    left: 110px; top: 380px;
    width: 270px; height: 100px;
  }
  .neck-band .neck-oval {
    position: absolute;
    left: 95px; top: -22px;
    width: 80px; height: 144px;
    border-radius: 50%;
    background: var(--oval-orange);
    border: 4px solid var(--frame-white);
    display: flex; align-items: center; justify-content: center;
  }
  .neck-oval .lock-art {
    width: 48px; height: 62px;
    border-radius: 22px 22px 18px 18px;
  }

  /* Body label */
  .body-label {
    position: absolute;
    left: 460px; top: 110px;
    width: 440px; height: 680px;
  }
  .label-oval {
    position: absolute;
    left: 22px; top: 50px;
    width: 396px; height: 560px;
    border-radius: 50%;
    border: 7px solid var(--frame-white);
    background: radial-gradient(ellipse at 50% 45%, var(--oval-orange) 55%, var(--oval-orange-deep) 100%);
  }
  .apple-badge {
    position: absolute;
    left: 183px; top: 14px;
    width: 74px; height: 74px;
    border-radius: 50%;
    background: var(--frame-white);
    display: flex; align-items: center; justify-content: center;
  }
  .apple-badge .apple-art {
    width: 56px; height: 44px;
    border-radius: 50%;
    background: radial-gradient(circle at 40% 40%, #e86a4a, var(--apple-red) 70%);
  }
  .brand-name {
    position: absolute;
    left: 0; right: 0; top: 96px;
    text-align: center;
    font-family: "Rye", Georgia, serif;
    color: var(--title-red);
    line-height: 1;
  }
  .brand-name .line-1 { display: block; font-size: 50px; }
  .brand-name .line-2 { display: block; font-size: 56px; margin-top: 6px; }
  .product-type {
    position: absolute;
    left: 125px; top: 232px;
    width: 190px; height: 26px;
    border-radius: 6px;
    background: var(--pill-red);
    color: var(--frame-white);
    font-size: 18px;
    letter-spacing: 2px;
    text-align: center;
    line-height: 26px;
  }
  .lock-art {
    background: radial-gradient(ellipse at 50% 55%, var(--lock-gold) 30%, var(--lock-olive) 100%);
  }
  .body-label .lock-art {
    position: absolute;
    left: 95px; top: 275px;
    width: 250px; height: 310px;
    border-radius: 120px 120px 110px 110px;
  }
  .volume {
    position: absolute;
    left: 14px; top: 628px;
    font-size: 26px;
    color: var(--ink);
  }
  .abv {
    position: absolute;
    right: 14px; top: 636px;
    font-size: 15px;
    color: var(--ink);
  }
</style>
</head>
<body>
  <div class="neck-band striped">
    <div class="neck-oval">
      <div class="lock-art" role="img" aria-label="Small engraved gold padlock illustration"></div>
    </div>
  </div>

  <div class="body-label striped">
    <div class="label-oval"></div>
    <div class="apple-badge">
      <div class="apple-art" role="img" aria-label="Illustration of red apples with a cut half"></div>
    </div>
    <h1 class="brand-name">
      <span class="line-1">THE LARK</span>
      <span class="line-2">HOLLOW</span>
    </h1>
    <div class="product-type">APPLE CIDER</div>
    <div class="lock-art" role="img" aria-label="Ornate engraved gold padlock illustration with keyhole"></div>
    <div class="volume">330 ml</div>
    <div class="abv">ALC 4.5% VOL</div>
  </div>
</body>
</html>
```